Sunny Paths and joy Business card

I have a logo, but will like a business card design. Is for a travel agency in Mexico. We focus in family experiences.

I will liek some thing different and unique, from the traditional business card, something to get remmeber for.

Business card information:

Leandro T. Ocampo
leandro@sunnypathsjoy.example

Alameda 482, 3 piso
Col. Tlalpizco
Mexico, D.F. 07320

office: (55) 5000-0142
mobile: (55) 9000-0187

www.sunnypathsjoy.example
@sunnypjoy
blog: sunnypathsandjoy.blogsite.example
facebook: SunnyPathsAndJoy

```html
<!DOCTYPE html>
<html lang="en">
<head>
<meta charset="utf-8">
<title>Sunny Paths and joy – Business card</title>
<link rel="stylesheet" href="https://fonts.googleapis.com/css2?family=Exo+2:wght@400;600;800&display=swap">
<style>
  :root {
    --page: #e6e6e6;
    --card: #ffffff;
    --brand-blue: #0b5cb8;
    --edge-blue: #7fb0e6;
    --ink-dark: #1d3f77;
    --ink: #1b1b1b;
    --sky: #cfe3f7;
  }
  * { box-sizing: border-box; margin: 0; padding: 0; }
  html, body { width: 1200px; height: 900px; overflow: hidden; }
  body {
    background: var(--page);
    font-family: "Exo 2", sans-serif;
    position: relative;
  }
  .card {
    position: absolute;
    width: 660px;
    height: 380px;
    background: var(--card);
    overflow: hidden;
  }
  .card svg.card-shape { position: absolute; inset: 0; }
  .card-back { left: 70px; top: 60px; }
  .card-front { left: 470px; top: 480px; }

  .holder-name {
    position: absolute; left: 34px; top: 100px;
    color: #fff; font-size: 19px; font-weight: 600;
  }
  .postal {
    position: absolute; left: 48px; top: 268px;
    color: #fff; font-size: 15px; line-height: 19px; font-weight: 400;
  }
  .postal .phones { margin-top: 19px; }

  .brand {
    position: absolute;
    display: flex; align-items: center; gap: 10px;
  }
  .brand-dot {
    width: 44px; height: 44px; border-radius: 50%;
    background: var(--sky); flex: none;
  }
  .brand-name {
    color: var(--ink-dark); font-weight: 800;
    font-size: 30px; line-height: 1; white-space: nowrap;
  }
  .card-back .brand { left: 320px; top: 120px; }
  .card-back .brand-name { font-size: 26px; }
  .card-front .brand { left: 50%; top: 150px; transform: translateX(-50%); }
  .card-front .brand-dot { width: 56px; height: 56px; }
  .card-front .brand-name { font-size: 40px; }

  .contact-lines {
    position: absolute; right: 34px; top: 268px;
    text-align: right; color: var(--ink);
    font-size: 15px; line-height: 18px;
  }
  .site-url {
    position: absolute; right: 24px; bottom: 24px;
    color: #fff; font-size: 24px; font-weight: 600;
  }
</style>
</head>
<body>
  <section class="card card-back" aria-label="Card back with contact details">
    <svg class="card-shape" width="660" height="380" viewBox="0 0 660 380" aria-hidden="true">
      <path d="M0 0 H258 C238 60 282 120 276 190 C270 260 252 320 298 380 H0 Z" fill="var(--edge-blue)"/>
      <path d="M0 0 H250 C230 60 274 120 268 190 C262 260 244 320 290 380 H0 Z" fill="var(--brand-blue)"/>
    </svg>
    <p class="holder-name">Leandro T. Ocampo</p>
    <div class="postal">
      <p>Alameda 482, 3 piso</p>
      <p>Col. Tlalpizco</p>
      <p>Mexico, D.F. 07320</p>
      <div class="phones">
        <p>office: (55) 5000-0142</p>
        <p>mobile: (55) 9000-0187</p>
      </div>
    </div>
    <div class="brand">
      <span class="brand-dot"></span>
      <span class="brand-name">Sunny Paths and joy</span>
    </div>
    <div class="contact-lines">
      <p>leandro@sunnypathsjoy.example</p>
      <p>www.sunnypathsjoy.example</p>
      <p>@sunnypjoy</p>
      <p>blog: sunnypathsandjoy.blogsite.example</p>
      <p>facebook: SunnyPathsAndJoy</p>
    </div>
  </section>

  <section class="card card-front" aria-label="Card front with brand">
    <svg class="card-shape" width="660" height="380" viewBox="0 0 660 380" aria-hidden="true">
      <path d="M0 290 C180 292 380 262 660 276 V380 H0 Z" fill="var(--edge-blue)"/>
      <path d="M0 298 C180 300 380 270 660 284 V380 H0 Z" fill="var(--brand-blue)"/>
    </svg>
    <div class="brand">
      <span class="brand-dot"></span>
      <span class="brand-name">Sunny Paths and joy</span>
    </div>
    <p class="site-url">www.sunnypathsjoy.example</p>
  </section>
</body>
</html>
```